Lock Company Van

The Crestmoor Lock Company needs a design for the side and back of our service vans.
Updates

Target Market(s)

B2B, Retail Stores, Individual Customers

Industry/Entity Type

Locksmith

Requirements
Must have
• "Protect yourself with THE CRESTMOOR" as a tagline.

```html
<!DOCTYPE html>
<html lang="en">
<head>
<meta charset="utf-8">
<title>The Crestmoor Lock Company – Van Wrap</title>
<link href="https://fonts.googleapis.com/css2?family=Open+Sans:ital,wght@0,700;1,700&display=swap" rel="stylesheet">
<style>
  :root {
    --crimson: #c21d3a;
    --crimson-dark: #8e1f2b;
    --blush: #e8b3a0;
    --slate: #5a5d63;
    --slate-light: #a9a8ae;
    --ink: #1f2a36;
    --paper: #ffffff;
  }
  html, body {
    margin: 0;
    width: 1200px;
    height: 1200px;
    overflow: hidden;
    background: var(--paper);
  }
  .van-wrap { display: block; width: 1200px; height: 1200px; }
  .brand-name { font-family: "Open Sans", sans-serif; font-weight: 700; fill: var(--crimson); }
  .tagline { font-family: "Open Sans", sans-serif; font-weight: 700; font-style: italic; fill: var(--slate); }
  .call-label, .call-number { font-family: "Open Sans", sans-serif; font-weight: 700; font-style: italic; fill: var(--paper); }
  .panel-outline { fill: none; stroke: #000; stroke-width: 2.5; }
  .cutout { fill: var(--paper); stroke: #000; stroke-width: 2.5; }
</style>
</head>
<body>
<svg class="van-wrap" viewBox="0 0 1445 1445" xmlns="http://www.w3.org/2000/svg">
  <defs>
    <linearGradient id="red-sweep" x1="0" y1="1" x2="1" y2="0">
      <stop offset="0" stop-color="var(--blush)"/>
      <stop offset="0.25" stop-color="var(--crimson)"/>
      <stop offset="0.8" stop-color="var(--crimson)"/>
      <stop offset="1" stop-color="var(--crimson-dark)"/>
    </linearGradient>
    <linearGradient id="red-band" x1="0" y1="0" x2="1" y2="0">
      <stop offset="0" stop-color="var(--crimson-dark)"/>
      <stop offset="0.15" stop-color="var(--crimson)"/>
      <stop offset="0.85" stop-color="var(--crimson)"/>
      <stop offset="1" stop-color="#d9705f"/>
    </linearGradient>
    <linearGradient id="red-top-right" x1="0" y1="0" x2="1" y2="0">
      <stop offset="0" stop-color="var(--crimson-dark)"/>
      <stop offset="0.3" stop-color="var(--crimson)"/>
      <stop offset="0.85" stop-color="var(--crimson)"/>
      <stop offset="1" stop-color="var(--blush)"/>
    </linearGradient>
    <linearGradient id="grey-strip" x1="0" y1="0" x2="1" y2="0">
      <stop offset="0" stop-color="var(--slate)"/>
      <stop offset="0.5" stop-color="var(--slate)"/>
      <stop offset="1" stop-color="var(--slate-light)"/>
    </linearGradient>
    <linearGradient id="grey-swoosh" x1="0" y1="0" x2="1" y2="0">
      <stop offset="0" stop-color="var(--slate-light)"/>
      <stop offset="1" stop-color="var(--slate)"/>
    </linearGradient>
  </defs>

  <!-- Rear panel -->
  <g class="rear-panel">
    <path d="M30 782 L34 740 Q50 560 95 505 L663 505 Q700 600 727 782 Z" fill="var(--paper)"/>
    <path class="top-swoosh" d="M95 505 L640 505 Q320 530 34 740 Q50 560 95 505 Z" fill="url(#red-sweep)"/>
    <path class="panel-outline" d="M30 782 L34 740 Q50 560 95 505 L663 505 Q700 600 727 782"/>
    <line x1="595" y1="490" x2="595" y2="782" stroke="#e4e4e4" stroke-width="1"/>
    <rect class="call-band" x="30" y="782" width="697" height="126" fill="url(#red-band)"/>
    <path class="cutout" d="M30 782 L68 782 Q82 782 82 796 L82 894 Q82 908 68 908 L30 908 Z"/>
    <rect class="cutout" x="408" y="800" width="176" height="96" rx="12"/>
    <rect class="strip" x="30" y="908" width="697" height="35" fill="url(#grey-strip)"/>

    <circle cx="380" cy="620" r="34" fill="var(--crimson)"/>
    <text class="brand-name" x="380" y="718" font-size="40" text-anchor="middle">THE CRESTMOOR</text>
    <text class="brand-name" x="380" y="744" font-size="20" text-anchor="middle" letter-spacing="3">LOCK COMPANY</text>
    <text class="tagline" x="380" y="771" font-size="14.5" text-anchor="middle">PROTECT YOURSELF WITH THE CRESTMOOR</text>

    <text class="call-label" x="102" y="843" font-size="31" transform="rotate(-7 102 843)">CALL US!</text>
    <text class="call-number" x="122" y="888" font-size="41">9999 999 999</text>
  </g>

  <!-- Side panel -->
  <g class="side-panel">
    <rect x="727" y="505" width="698" height="438" fill="var(--paper)"/>
    <path class="grey-swoosh" d="M727 505 L1080 528 Q860 585 727 690 Z" fill="url(#grey-swoosh)"/>
    <path class="red-swoosh" d="M880 505 L1425 505 L1425 662 Q1260 540 1080 528 Z" fill="url(#red-top-right)"/>
    <path class="bottom-wave" d="M727 782 Q770 780 815 825 Q870 878 1000 878 L1425 878 L1425 908 L727 908 Z" fill="url(#red-band)"/>
    <rect class="strip" x="727" y="908" width="698" height="35" fill="url(#grey-strip)"/>
    <rect x="727" y="505" width="698" height="438" fill="none" stroke="var(--crimson)" stroke-width="2"/>
    <rect class="cutout" x="678" y="783" width="75" height="125" rx="12"/>

    <circle cx="1076" cy="660" r="46" fill="var(--crimson)"/>
    <text class="brand-name" x="1076" y="783" font-size="52" text-anchor="middle">THE CRESTMOOR</text>
    <text class="brand-name" x="1076" y="815" font-size="26" text-anchor="middle" letter-spacing="4">LOCK COMPANY</text>
    <text class="tagline" x="1078" y="849" font-size="19" text-anchor="middle">PROTECT YOURSELF WITH THE CRESTMOOR</text>
  </g>
</svg>
</body>
</html>
```